Corvelle Solutions needs an IT Managed Services Website and the logo needs to be updated

We need a new website for our 25 year old IT Managed Services Company. Our company specializes in listening to and understanding our customer needs and goals. Our customers include SME's and Corporates in industries ranging from Medical, Legal, Industrial & Manufacturing and Financial. The services that we offer include: Managed IT Services, Remote Monitoring and Management and Virtualisation. Corvelle Solutions takes technology and makes the lives of our customers easier by applying it appropriately. In the same way, we want a website that is as pleasing to the eye, as it is simple to find information and call to action. The website should say as much in design as it does in content and it should be saying that Corvelle Solutions is your technology partner that listens to you, understands you, delivers solutions and is loyal in our relationship with you. Aesthetically, we want to go for something a little warmer than blue and white, but want to err on the side of professional.
The Logo: We need the "computer" and "ltd" to be removed from the logo. We want to keep the @ on the "u". We would like to freshen up the logo inline with the website design in terms of look and feel and colour.

Target Market(s)

Businesses that require IT Managed Services

Logo Text

Corvelle Solutions

Coding

Coded - Design and coding required

Number of Pages Required

5+ page

Font styles to use
Sans Serif

Colors

Designer to choose colors to be used in the design.

Requirements
Must have
• Each page must have a call to action.

```html
<!DOCTYPE html>
<html lang="en">
<head>
<meta charset="utf-8">
<title>Corvelle Solutions – IT Managed Services</title>
<link rel="stylesheet" href="https://fonts.googleapis.com/css2?family=Oswald:wght@400;500;600;700&family=Montserrat:wght@700;800&family=Roboto:wght@300;400;500;700&display=swap">
<style>
:root{
  --blue:#1266e6;
  --blue-deep:#0a4fc0;
  --cyan:#1fb8e8;
  --navy:#0d1b2e;
  --ink:#1c2330;
  --text:#4a5260;
  --muted:#7a828f;
  --light:#eef7fa;
  --grey:#f4f5f7;
  --dark:#222427;
  --white:#ffffff;
  --placeholder:#c3c9d0;
}
*{box-sizing:border-box;margin:0;padding:0}
html,body{width:1200px;height:3805px;overflow:hidden}
body{font-family:'Roboto',sans-serif;color:var(--text);background:var(--white);position:relative}
section,header,footer{position:absolute;left:0;width:1200px;overflow:hidden}
.abs{position:absolute}
.btn{position:absolute;display:flex;align-items:center;justify-content:center;border-radius:40px;font-family:'Roboto',sans-serif;font-weight:700;font-size:12px;letter-spacing:1px;text-transform:uppercase}
.btn--blue{background:var(--blue);color:var(--white)}
.btn--white{background:var(--white);color:var(--blue)}
.heading{font-family:'Oswald',sans-serif;font-weight:600;text-transform:uppercase;letter-spacing:2px}

/* hero */
.hero{top:0;height:528px;background:linear-gradient(180deg,#5d7286 0%,#3a4b5d 45%,#1c2633 100%)}
.hero__photo{position:absolute;inset:0;background:radial-gradient(ellipse at 50% 35%,rgba(190,210,225,.35),rgba(20,30,45,0) 60%)}
.nav__brand{left:254px;top:14px;display:flex;align-items:center;gap:8px;font-family:'Roboto',sans-serif;font-weight:700;font-size:20px;color:var(--white)}
.nav__brand i{width:26px;height:26px;border-radius:50%;background:var(--blue);display:block}
.nav__brand small{display:block;font-size:9px;font-weight:400}
.nav__menu{left:495px;top:29px;display:flex;gap:14px;font-size:9.5px;font-weight:700;color:var(--white);text-transform:uppercase;letter-spacing:.3px;white-space:nowrap}
.nav__search{left:806px;top:27px}
.nav__signin{left:842px;top:18px;width:110px;height:32px}
.hero__title{left:0;width:1200px;top:285px;text-align:center;color:var(--white);font-size:64px;letter-spacing:4px;font-weight:600;line-height:80px}
.hero__sub{left:0;width:1200px;top:362px;text-align:center;color:var(--white);font-family:'Oswald',sans-serif;font-size:34px;letter-spacing:6px;font-weight:400;line-height:44px}
.hero__line{left:0;width:1200px;top:414px;text-align:center;color:var(--white);font-size:16px;letter-spacing:1.5px;line-height:22px}
.hero__cta{left:520px;top:460px;width:148px;height:34px}

/* experience */
.experience{top:528px;height:340px;background:linear-gradient(135deg,#f3fbfd 0%,#dff1f7 50%,#c9e9f2 100%)}
.experience__big{left:254px;top:58px;font-family:'Oswald',sans-serif;font-weight:700;font-size:64px;line-height:68px;text-transform:uppercase;background:linear-gradient(180deg,var(--blue-deep),var(--cyan));-webkit-background-clip:text;background-clip:text;color:transparent}
.experience__title{left:647px;top:56px;font-size:24px;color:var(--ink)}
.experience__text{left:647px;top:94px;width:310px;font-size:12px;line-height:17px}
.experience__cta{left:647px;top:215px;width:145px;height:38px}

/* services */
.services{top:868px;height:434px;background:var(--blue);display:flex}
.service{position:relative;width:400px;height:434px;text-align:center;color:var(--white);padding-top:70px}
.service--first{background:var(--blue-deep)}
.service--dark{background:var(--dark);width:378px;margin:10px 11px;height:414px;padding-top:60px;border:2px solid #333}
.service__icon{display:block;margin:0 auto}
.service__title{margin-top:46px;font-family:'Oswald',sans-serif;font-weight:600;font-size:18px;letter-spacing:2px;text-transform:uppercase}
.service__text{margin:14px auto 0;width:330px;font-size:11px;line-height:17px}
.service__cta{position:relative;margin:22px auto 0;width:150px;height:42px;display:flex}

/* why us */
.why{top:1302px;height:596px;background:var(--white)}
.why__title{left:170px;top:132px;font-size:44px;color:var(--blue)}
.why__lead{left:170px;top:190px;width:450px;font-size:19px;line-height:28px;color:var(--ink)}
.why__text{left:170px;top:292px;width:440px;font-size:11px;line-height:17px}
.why__cta{left:170px;top:443px;width:148px;height:44px}
.why__screen{left:723px;top:68px;width:368px;height:457px;background:linear-gradient(160deg,#1a1c20 0%,#3a4250 40%,#d7dde3 75%,#f2f4f6 100%);border-radius:10px}

/* testimonials */
.testimonials{top:1898px;height:373px;background:linear-gradient(135deg,#0b47b8 0%,#1466e0 50%,#0b4ebd 100%);text-align:center;color:var(--white)}
.testimonials__title{left:0;width:1200px;top:58px;font-size:44px}
.testimonials__quote{left:0;width:1200px;top:116px;font-family:'Oswald',sans-serif;font-size:52px;line-height:52px}
.testimonials__text{left:305px;width:590px;top:172px;font-size:15px;line-height:24px}
.testimonials__name{left:0;width:1200px;top:252px;font-weight:700;font-size:12px;letter-spacing:1px}
.testimonials__role{left:0;width:1200px;top:270px;font-size:9px;letter-spacing:1px}
.testimonials__dots{left:578px;top:305px;display:flex;gap:8px}
.testimonials__dots i{width:8px;height:8px;border-radius:50%;background:var(--white);display:block}

/* blogs */
.blogs{top:2271px;height:748px;background:var(--grey)}
.blogs__title{left:0;width:1200px;top:44px;text-align:center;font-size:44px;color:var(--blue)}
.post{position:absolute;background:var(--white)}
.post--feature{left:152px;top:152px;width:300px;height:500px;box-shadow:0 4px 14px rgba(0,0,0,.18)}
.post__img{display:block;background:linear-gradient(135deg,#c9cfd4,#6f7882 60%,#3b424b)}
.post__body{padding:14px 16px}
.post__title{font-family:'Montserrat',sans-serif;font-weight:800;font-size:19px;line-height:22px;color:var(--ink);text-transform:uppercase}
.post__date{margin-top:10px;font-size:8px;color:var(--muted);text-transform:uppercase}
.post__text{margin-top:8px;font-size:9px;line-height:13px}
.post__more{margin-top:10px;font-size:9px;font-weight:700;color:var(--ink);text-transform:uppercase}

/* partners */
.partners{top:3019px;height:216px;background:linear-gradient(135deg,#d9f1f6,#b6e3ee 60%,#d6f0f5)}
.partners__strip{left:241px;top:64px;width:718px;height:94px;background:var(--white);display:flex;align-items:center;justify-content:space-around;padding:0 30px}
.partner{display:block;width:96px;height:40px;border-radius:6px;background:var(--placeholder)}

/* newsletter */
.newsletter{top:3235px;height:296px;background:#2a2c30}
.newsletter__photo{left:660px;top:0;width:540px;height:296px;background:linear-gradient(90deg,#2a2c30 0%,#4a4f56 45%,#6b7178 100%)}
.newsletter__bar{left:254px;top:70px;width:3px;height:170px;background:var(--white)}
.newsletter__title{left:266px;top:66px;width:360px;font-size:28px;line-height:28px;color:var(--white);letter-spacing:1px}
.newsletter__text{left:266px;top:140px;width:320px;font-size:13px;line-height:17px;color:#d8dadd}
.newsletter__input{left:266px;top:194px;width:262px;height:32px;background:var(--white);color:#9a9fa6;font-size:10px;padding:0 10px;display:flex;align-items:center}
.newsletter__submit{left:528px;top:194px;width:120px;height:32px;background:var(--blue);color:var(--white);font-size:8px;font-weight:700;display:flex;align-items:center;justify-content:center;letter-spacing:.5px}

/* footer */
.footer{top:3531px;height:274px;background:var(--blue);color:var(--white);text-align:center}
.footer__social{left:536px;top:45px;display:flex;gap:12px}
.footer__social i{width:40px;height:40px;border-radius:50%;background:#5b95ee;display:block}
.footer__contact{left:0;width:1200px;top:102px;display:flex;justify-content:center;gap:36px;font-size:12px}
.footer__contact span{display:flex;align-items:center;gap:6px}
.footer__menu{left:0;width:1200px;top:138px;display:flex;justify-content:center;gap:22px;font-size:11px;font-weight:700;text-transform:uppercase}
.footer__brand{left:0;width:1200px;top:168px;font-family:'Oswald',sans-serif;font-weight:600;font-size:17px;letter-spacing:1px;text-transform:uppercase}
.footer__copy{left:0;width:1200px;top:214px;font-size:9px}
</style>
</head>
<body>

<header class="hero">
  <div class="hero__photo" role="img" aria-label="Photo of business people meeting in front of a city skyline window"></div>
  <div class="abs nav__brand"><i></i><div>Corvelle<small>Solutions</small></div></div>
  <nav class="abs nav__menu"><span>Home</span><span>About Us</span><span>Services</span><span>Testimonials</span><span>Contact</span></nav>
  <svg class="abs nav__search" width="14" height="14" viewBox="0 0 16 16" fill="none" stroke="#fff" stroke-width="2"><circle cx="6.5" cy="6.5" r="5"/><line x1="10.5" y1="10.5" x2="15" y2="15"/></svg>
  <div class="btn btn--blue nav__signin">Sign In</div>
  <h1 class="abs heading hero__title">Free Choices Become</h1>
  <p class="abs hero__sub">THE MATRIX OF HUMAN LIFE</p>
  <p class="abs hero__line">Corvelle Solutions is an IT Managed Services Provider</p>
  <div class="btn btn--blue hero__cta">Contact Us</div>
</header>

<section class="experience">
  <div class="abs experience__big">25<br>Years<br>Experience</div>
  <h2 class="abs heading experience__title">Corvelle Solutions</h2>
  <p class="abs experience__text">growing and collaborating in the IT industry. Our expertise lies in listening to and understanding our more than 1500 customers' needs and delivering the best value for money IT infrastructure and Technology solutions. We believe in loyal and lasting relationships creating a matrix within which your company can grow and outperform its own expectations.</p>
  <div class="btn btn--blue experience__cta">Read More</div>
</section>

<section class="services">
  <div class="service service--first">
    <svg class="service__icon" width="100" height="96" viewBox="0 0 100 96" fill="none" stroke="#fff" stroke-width="3"><rect x="8" y="50" width="24" height="30" rx="4"/><rect x="38" y="44" width="24" height="36" rx="4"/><rect x="68" y="50" width="24" height="30" rx="4"/><line x1="50" y1="8" x2="50" y2="44"/><line x1="20" y1="26" x2="80" y2="26"/><line x1="20" y1="26" x2="20" y2="50"/><line x1="80" y1="26" x2="80" y2="50"/><line x1="4" y1="88" x2="96" y2="88"/></svg>
    <h3 class="service__title">Managed IT Services</h3>
    <p class="service__text">Corvelle brings a personal touch to you through our IT consulting services. We collaborate with partners across the globe to bring the best technology to you. You can rely on our expertise to design and maintain the most effective infrastructure for your business. Our quick and efficient Support team will troubleshoot your IT.</p>
    <div class="btn btn--white service__cta">Contact Us Now</div>
  </div>
  <div class="service service--dark">
    <svg class="service__icon" width="100" height="96" viewBox="0 0 100 96" fill="none" stroke="#fff" stroke-width="3"><circle cx="56" cy="36" r="24"/><circle cx="56" cy="36" r="9"/><circle cx="28" cy="68" r="14"/><circle cx="28" cy="68" r="5"/><line x1="56" y1="6" x2="56" y2="12"/><line x1="56" y1="60" x2="56" y2="66"/><line x1="26" y1="36" x2="32" y2="36"/><line x1="80" y1="36" x2="86" y2="36"/></svg>
    <h3 class="service__title">Remote Monitoring &amp; Management</h3>
    <p class="service__text">Corvelle brings you an all-encompassing service that includes managed antivirus, web protection, backup &amp; recovery and email security. You will be able to manage all devices including mobile and you will have active discovery on the network – identifying and managing all new devices that come onto the network.</p>
    <div class="btn btn--white service__cta">Contact Us Now</div>
  </div>
  <div class="service">
    <svg class="service__icon" width="100" height="96" viewBox="0 0 100 96" fill="none" stroke="#fff" stroke-width="3"><path d="M22 6h40l14 14v66H22z"/><line x1="32" y1="30" x2="64" y2="30"/><line x1="32" y1="40" x2="64" y2="40"/><line x1="32" y1="50" x2="50" y2="50"/><circle cx="72" cy="70" r="14"/><circle cx="72" cy="70" r="5"/></svg>
    <h3 class="service__title">Virtualisation</h3>
    <p class="service__text">Corvelle brings you the high performance Hyper Cloud, which reduces your total IT spend in comparison to competitors like Nimbus, Strato and Cirra. You will find that these Virtual Machines are easy to configure and migration is simple. With Enterprise Grade security and compliance you will have.</p>
    <div class="btn btn--white service__cta">Contact Us Now</div>
  </div>
</section>

<section class="why">
  <h2 class="abs heading why__title">Why Us</h2>
  <p class="abs why__lead">Corvelle Solutions was founded in 2000 and is in the business of collaborating with partners to bring the best technologies to you.</p>
  <div class="abs why__text">
    <p>We have more than 25 years experience in the IT industry servicing customers across the GTA and Ontario. Our customers come from different industry sectors including Medical, Financial, Real Estate, Legal and more. We work together with our customers as members of their teams to realize their IT vision and goals.</p>
    <p style="margin-top:10px">We have collaborated with partners across the globe to ensure that we bring the most innovate and functional technology to our customers. We can proudly say that we offer the best Value for Money solutions.</p>
  </div>
  <div class="btn btn--blue why__cta">Read More</div>
  <div class="abs why__screen" role="img" aria-label="Desktop monitor showing a photo of businesspeople in discussion"></div>
</section>

<section class="testimonials">
  <h2 class="abs heading testimonials__title">Testimonials</h2>
  <div class="abs testimonials__quote">&#8221;</div>
  <p class="abs testimonials__text">Lorem Ipsum is simply dummy text of the printing and typesetting industry. Lorem Ipsum has been the industry's standard dummy text ever since the 1500s, when an unknown printer took a galley of type and scrambled it to make a type specimen book</p>
  <p class="abs testimonials__name">MARA QUINT</p>
  <p class="abs testimonials__role">BUSINESSWOMAN</p>
  <div class="abs testimonials__dots"><i></i><i></i><i></i></div>
</section>

<section class="blogs">
  <h2 class="abs heading blogs__title">Latest Blogs</h2>
  <article class="post post--feature">
    <div class="post__img" style="height:246px" role="img" aria-label="Photo of hands working on a tablet and documents"></div>
    <div class="post__body">
      <h3 class="post__title">Lorem Ipsum is simply dummy text</h3>
      <p class="post__date">30 March 2018</p>
      <p class="post__text">Lorem Ipsum is simply dummy text of the printing and typesetting industry. Lorem Ipsum has been the industry's standard dummy text ever since the 1500s, when an unknown printer took a galley of type and scrambled it to make a type specimen book. It has survived not only five centuries, but also the leap into electronic typesetting, remaining essentially unchanged.</p>
      <p class="post__more">+ Read More</p>
    </div>
  </article>
  <article class="post" style="left:467px;top:203px;width:290px;height:394px">
    <div class="post__img" style="height:203px;background:linear-gradient(135deg,#dfe5ea,#8a96a3 55%,#2f3944)" role="img" aria-label="Photo of a team meeting around a table"></div>
    <div class="post__body">
      <h3 class="post__title">Lorem Ipsum is simply dummy text</h3>
      <p class="post__date">30 March 2018</p>
      <p class="post__text">Lorem Ipsum is simply dummy text of the printing and typesetting industry. Lorem Ipsum has been the industry's standard dummy text ever since the 1500s, when an unknown printer took a galley of type and scrambled it to make a type specimen book.</p>
      <p class="post__more">+ Read More</p>
    </div>
  </article>
  <article class="post" style="left:761px;top:203px;width:292px;height:414px">
    <div class="post__body">
      <h3 class="post__title">Lorem Ipsum is simply dummy text</h3>
      <p class="post__date">30 March 2018</p>
      <p class="post__text">Lorem Ipsum is simply dummy text of the printing and typesetting industry. Lorem Ipsum has been the industry's standard dummy text ever since the 1500s, when an unknown printer took a galley of type and scrambled it to make a type specimen book.</p>
      <p class="post__more">+ Read More</p>
    </div>
    <div class="post__img" style="position:absolute;left:0;top:208px;width:292px;height:206px;background:linear-gradient(135deg,#e9ecef,#9aa4ae 50%,#3a4350)" role="img" aria-label="Photo of a businessman working at a laptop"></div>
  </article>
</section>

<section class="partners">
  <div class="abs partners__strip">
    <span class="partner" role="img" aria-label="Partner badge"></span>
    <span class="partner" role="img" aria-label="Partner badge"></span>
    <span class="partner" role="img" aria-label="Partner badge"></span>
    <span class="partner" role="img" aria-label="Partner badge"></span>
    <span class="partner" role="img" aria-label="Partner badge"></span>
  </div>
</section>

<section class="newsletter">
  <div class="abs newsletter__photo" role="img" aria-label="Photo of a businessman in glasses looking at a laptop"></div>
  <div class="abs newsletter__bar"></div>
  <h2 class="abs heading newsletter__title">Sign me up for the newsletter</h2>
  <p class="abs newsletter__text">Lorem ipsum dolor sit amet, consectetur adipiscing elit, sed do eiusmod tempor incididunt ut labore et dolore magna aliqua. Ut enim ad minim veniam.</p>
  <div class="abs newsletter__input">Email Address</div>
  <div class="abs newsletter__submit">SIGN UP NOW</div>
</section>

<footer class="footer">
  <div class="abs footer__social"><i></i><i></i><i></i></div>
  <div class="abs footer__contact">
    <span><svg width="10" height="14" viewBox="0 0 10 14"><path d="M5 0a5 5 0 0 0-5 5c0 4 5 9 5 9s5-5 5-9a5 5 0 0 0-5-5zm0 7a2 2 0 1 1 0-4 2 2 0 0 1 0 4z" fill="#fff"/></svg>Lorem Ipsum is simply dummy text</span>
    <span><svg width="14" height="10" viewBox="0 0 14 10" fill="none" stroke="#fff" stroke-width="1.4"><rect x="1" y="1" width="12" height="8"/><path d="M1 1l6 5 6-5"/></svg>info@corvellesolutions.com</span>
  </div>
  <nav class="abs footer__menu"><span>Home</span><span>About Us</span><span>Services</span><span>Testimonials</span><span>Contact</span></nav>
  <p class="abs footer__brand">Corvelle Solutions</p>
  <p class="abs footer__copy">Copyright © 2018 <b>Corvelle Solutions</b>. All Rights Reserved</p>
</footer>

</body>
</html>
```